Magnetic Business card Design do a service provider

Hi,

The company aim is to provide all service needs under one roof. However, at the moment there is only Accounting, Electrical and IT branches. There will be more services coming onboard in the future.

I already have a logo designed (Company name is already part of the logo), I now need a magnetic business card designed.

The business card will contain the following:

- Company Logo
- Contact#
- E-mail
- enough space to add website URL (for future)
Updates

Project Deadline Extended Reason: HI All,The deadline has been extended due to not having enough time to review an overwhelming number of designs that has been submitted by lots of designers.I will be uploading a draft of designs that i have in mind.Thanks. Added Friday, January 22, 2016

Target Market(s)

Residential, Home-based Businesses, Small and Medium businesses

Industry/Entity Type

Business

Contact Information for Business Card

Contact#: 0491 738 520
E-mail: service@brightlanetrades.net.au

Font styles to use
Decorative
Script

Requirements
Must have
• Round edges
• Some form of logo incorporation as a background

```html
<!DOCTYPE html>
<html lang="en">
<head>
<meta charset="utf-8">
<title>Bright Lane Trades – Business Card</title>
<link rel="stylesheet" href="https://fonts.googleapis.com/css2?family=Open+Sans:wght@400;600&display=swap">
<style>
  :root {
    --page-bg: #e9e7e4;
    --card-black: #141517;
    --card-edge: #1d1f22;
    --accent-blue: #1e6fc4;
    --text-white: #f2f2f2;
    --text-soft: #c9cacc;
    --divider: #8a8c90;
    --emblem-light: #5c5f63;
    --emblem-dark: #1a1b1d;
  }
  * { box-sizing: border-box; margin: 0; padding: 0; }
  html, body {
    width: 1200px;
    height: 787px;
    overflow: hidden;
    background: var(--page-bg);
    font-family: "Open Sans", Arial, sans-serif;
  }
  .canvas {
    position: relative;
    width: 1200px;
    height: 787px;
  }
  .card {
    position: absolute;
    top: 245px;
    width: 525px;
    height: 300px;
    border-radius: 18px;
    background: var(--card-black);
    border: 1px solid var(--card-edge);
    box-shadow: 0 10px 28px rgba(0,0,0,.22);
    overflow: hidden;
  }
  .card--back { left: 45px; }
  .card--front { left: 630px; }

  .back-emblem {
    position: absolute;
    left: -40px;
    top: -70px;
    width: 420px;
    height: 420px;
    border-radius: 50%;
    background: radial-gradient(circle at 45% 40%, var(--emblem-light) 0%, #34363a 45%, var(--emblem-dark) 75%);
    opacity: .85;
  }

  .brand {
    position: absolute;
    left: 0;
    right: 0;
    top: 92px;
    display: flex;
    align-items: center;
    justify-content: center;
    gap: 10px;
  }
  .brand-dot {
    width: 26px;
    height: 26px;
    border-radius: 50%;
    background: var(--accent-blue);
  }
  .brand-name {
    font-size: 25px;
    font-weight: 600;
    color: var(--text-white);
    letter-spacing: .5px;
  }

  .details {
    position: absolute;
    left: 38px;
    top: 178px;
    display: flex;
    align-items: flex-start;
  }
  .person {
    text-align: right;
    padding-right: 18px;
    padding-top: 6px;
  }
  .person-name {
    font-size: 17px;
    font-weight: 600;
    color: var(--accent-blue);
  }
  .person-title {
    font-size: 14px;
    color: var(--text-white);
    margin-top: 2px;
  }
  .divider {
    width: 1px;
    height: 78px;
    background: var(--divider);
  }
  .contact-list {
    list-style: none;
    padding-left: 16px;
  }
  .contact-item {
    display: flex;
    align-items: center;
    gap: 10px;
    font-size: 14px;
    line-height: 20px;
    color: var(--text-white);
    margin-bottom: 4px;
  }
  .contact-icon {
    width: 15px;
    height: 15px;
    flex: none;
    fill: var(--accent-blue);
  }
</style>
</head>
<body>
<main class="canvas">
  <section class="card card--back" aria-label="Card back">
    <div class="back-emblem" role="img" aria-label="Large faint company emblem used as background decoration"></div>
  </section>

  <section class="card card--front" aria-label="Card front">
    <div class="brand">
      <span class="brand-dot"></span>
      <span class="brand-name">Bright Lane Trades</span>
    </div>

    <div class="details">
      <div class="person">
        <p class="person-name">Mark Ellery</p>
        <p class="person-title">President</p>
      </div>
      <div class="divider"></div>
      <ul class="contact-list">
        <li class="contact-item">
          <svg class="contact-icon" viewBox="0 0 16 16" aria-hidden="true"><path d="M2 5c0-2 2-3 6-3s6 1 6 3v1.5h-3V5H5v1.5H2zM4 7h8l2 7H2zm4 1.8a2 2 0 100 4 2 2 0 000-4z"/></svg>
          <span>0491 738 520</span>
        </li>
        <li class="contact-item">
          <svg class="contact-icon" viewBox="0 0 16 16" aria-hidden="true"><path d="M1 3h14v1.5L8 9 1 4.5zM1 6.2l7 4.5 7-4.5V13H1z"/></svg>
          <span>service@brightlanetrades.net.au</span>
        </li>
        <li class="contact-item">
          <svg class="contact-icon" viewBox="0 0 16 16" aria-hidden="true"><circle cx="8" cy="8" r="7"/><path d="M1 8h14M8 1c2.5 2 2.5 12 0 14M8 1c-2.5 2-2.5 12 0 14" stroke="#141517" stroke-width="1" fill="none"/></svg>
          <span>www.brightlanetrades.net.au</span>
        </li>
      </ul>
    </div>
  </section>
</main>
</body>
</html>
```